Post it Note design

POST-IT NOTE DESIGN (CONTENT)
Size recommended: 4x6 for handwriting space.
Header (Bold):
Lighting Issue Detected on Your Property
Sub-header:
During our routine night inspection, we noted the following item(s):
Checkbox List:
⬜ Building Lights Out
⬜ Pole Lights Out
⬜ Sign Not Illuminated
⬜ Other ________________________
Action Line:
We can provide a quote or dispatch service right away.
Area for notes
Contact Block (Bold & Centered):
Brightwell Fixture Care Inc.
Service@BrightwellFixtureCare.com
www.BrightwellFixtureCare.com
877-514-6082
Industry/Entity Type
Electrical lighting
Colors
Designer to choose colors to be used in the design.
Look and feel
Each slider illustrates characteristics of the customer's brand and the style your logo design should communicate.

```html
<!DOCTYPE html>
<html lang="en">
<head>
<meta charset="utf-8">
<title>Lighting Issue Detected – Brightwell Fixture Care Inc.</title>
<link href="https://fonts.googleapis.com/css2?family=Poppins:wght@500;600;700;800&display=swap" rel="stylesheet">
<style>
  :root {
    --red: #c8202a;
    --red-deep: #a51b24;
    --blue: #2b3484;
    --navy: #252f7a;
    --white: #ffffff;
    --ink-red: #e0222b;
    --page: #eceef1;
    --rule: #1d1d2b;
  }
  * { margin: 0; padding: 0; box-sizing: border-box; }
  html, body { width: 1200px; height: 2866px; overflow: hidden; background: var(--page); }
  body { font-family: "Poppins", sans-serif; position: relative; }

  .note {
    position: absolute; left: 100px; top: 683px;
    width: 812px; height: 1218px;
    transform: scale(1.2315); transform-origin: 0 0;
    overflow: hidden; background: var(--white);
  }
  .note-bg { position: absolute; inset: 0; width: 812px; height: 1218px; }

  .headline {
    position: absolute; left: 32px; top: 36px;
    color: var(--white); font-weight: 700; font-size: 50px; line-height: 68px;
    letter-spacing: 0.2px; text-shadow: 0 2px 6px rgba(0,0,0,0.25);
  }

  .brand {
    position: absolute; left: 440px; top: 150px; width: 340px;
    text-align: center; color: var(--white);
    font-weight: 700; font-size: 38px; line-height: 44px;
  }

  .photo { position: absolute; border-radius: 14px; }
  .photo-truck {
    left: 115px; top: 320px; width: 420px; height: 265px;
    background: linear-gradient(160deg, #f4f5f7 0%, #d9dce2 70%, #b9bdc6 100%);
  }
  .photo-van {
    left: 568px; top: 355px; width: 218px; height: 155px;
    background: linear-gradient(160deg, #fafafa 0%, #dcdfe4 75%, #b8bcc4 100%);
  }

  .action {
    position: absolute; left: 446px; top: 432px; width: 336px; height: 336px;
    border-radius: 50%; background: var(--red-deep);
    display: flex; align-items: flex-end; justify-content: center;
    padding-bottom: 36px;
    color: var(--white); text-align: center;
    font-weight: 800; font-size: 29px; line-height: 45px;
  }
  .photo-van { z-index: 2; }

  .intro {
    position: absolute; left: 32px; top: 612px; width: 400px;
    color: var(--navy); font-weight: 700; font-size: 27px; line-height: 45px;
  }

  .section-title {
    position: absolute; color: var(--navy); font-weight: 700; font-size: 20px;
    text-decoration: underline; text-underline-offset: 3px;
  }
  .checklist-title { left: 32px; top: 795px; }
  .notes-title { left: 469px; top: 798px; }

  .checklist { position: absolute; left: 32px; top: 843px; list-style: none; }
  .checklist li {
    display: flex; align-items: center; height: 51px;
    color: var(--ink-red); font-weight: 600; font-size: 22px;
  }
  .checkbox {
    width: 11px; height: 13px; border: 1px solid var(--ink-red);
    margin-right: 9px; display: inline-block;
  }
  .other-line { letter-spacing: 2px; margin-left: 8px; color: var(--rule); }

  .notes-lines { position: absolute; left: 469px; top: 862px; width: 302px; }
  .notes-lines span { display: block; height: 39.5px; border-bottom: 1.5px solid var(--rule); }

  .contact {
    position: absolute; left: 0; right: 0; top: 1112px;
    text-align: center; color: var(--white);
  }
  .contact-name { font-weight: 700; font-size: 19px; line-height: 26px; }
  .contact-links { font-weight: 500; font-size: 19.5px; line-height: 30px; }
  .contact-links .sep { margin: 0 18px; }
  .contact-phone { font-weight: 800; font-size: 28px; line-height: 44px; }
</style>
</head>
<body>
  <article class="note">
    <svg class="note-bg" viewBox="0 0 812 1218" aria-hidden="true">
      <defs>
        <linearGradient id="blueGrad" x1="0" y1="0" x2="1" y2="1">
          <stop offset="0" stop-color="#3a4aa0"/>
          <stop offset="1" stop-color="#262e7c"/>
        </linearGradient>
        <linearGradient id="redGrad" x1="0" y1="0" x2="1" y2="1">
          <stop offset="0" stop-color="#c81f29"/>
          <stop offset="1" stop-color="#a81c24"/>
        </linearGradient>
      </defs>
      <rect width="812" height="560" fill="url(#blueGrad)"/>
      <path d="M0,0 L595,0 C470,110 360,250 310,330 C265,395 150,382 0,368 Z" fill="url(#redGrad)"/>
      <path d="M0,455 C120,540 300,560 450,520 C600,470 720,380 812,270 L812,1218 L0,1218 Z" fill="#ffffff"/>
      <path d="M0,1068 C260,1102 600,1062 812,970 L812,1218 L0,1218 Z" fill="var(--ink-red)"/>
      <path d="M0,1070 C260,1106 600,1078 812,1000 L812,1218 L0,1218 Z" fill="var(--navy)"/>
    </svg>

    <h1 class="headline">Lighting<br>Issue Detected<br>on Your<br>Property</h1>

    <div class="brand">Brightwell<br>Fixture Care Inc.</div>

    <div class="photo photo-truck" role="img" aria-label="Photo of a white bucket truck with lettered service body, parked behind orange traffic cones"></div>

    <div class="action">WE CAN<br>PROVIDE A QUOTE<br>OR DISPATCH<br>SERVICE RIGHT<br>AWAY.</div>

    <div class="photo photo-van" role="img" aria-label="Photo of a white service van with company lettering"></div>

    <p class="intro">During our routine night inspection, we noted the following item(s):</p>

    <h2 class="section-title checklist-title">CHECKBOX LIST:</h2>
    <ul class="checklist">
      <li><span class="checkbox"></span>Building Lights Out</li>
      <li><span class="checkbox"></span>Pole Lights Out</li>
      <li><span class="checkbox"></span>Sign Not Illuminated</li>
      <li><span class="checkbox"></span>Other <span class="other-line">____________</span></li>
    </ul>

    <h2 class="section-title notes-title">AREA FOR NOTES</h2>
    <div class="notes-lines"><span></span><span></span><span></span><span></span></div>

    <footer class="contact">
      <p class="contact-name">BRIGHTWELL FIXTURE CARE INC.</p>
      <p class="contact-links">Service@BrightwellFixtureCare.com<span class="sep">|</span>www.BrightwellFixtureCare.com</p>
      <p class="contact-phone">877-514-6082</p>
    </footer>
  </article>
</body>
</html>
```